Create A Visually Appealling Graphic

Take the concept from Power Point and add some wow to it....right now the graphic is very sterile and boring. Use Images if necessary to clearly show that everything is connected. Working together to bring a product to market......Open to all suggestions and creativity....the more creative the better

Target Market(s)

Inventors

Industry/Entity Type

Management Consulting

Requirements
Must have
• Visually appealing....images to complement the words in the graphic. Tagline at the bottom
Nice to have
• Cool looking, attention getting, simple look
Should not have
• be too complicated, too many colors

```html
<!DOCTYPE html>
<html lang="en">
<head>
<meta charset="utf-8">
<title>Innovation into the Market</title>
<link href="https://fonts.googleapis.com/css2?family=Montserrat:wght@700;800&display=swap" rel="stylesheet">
<style>
  :root {
    --brand-blue: #1d64ac;
    --brand-green: #22a94b;
    --paper: #ffffff;
  }
  html, body {
    margin: 0;
    padding: 0;
    width: 1200px;
    height: 1018px;
    overflow: hidden;
    background: var(--paper);
  }
  .cycle-diagram {
    display: block;
    width: 1200px;
    height: 1018px;
    font-family: "Montserrat", Arial, sans-serif;
  }
  .ring { fill: none; stroke: var(--brand-blue); stroke-width: 28; }
  .node { fill: var(--brand-blue); stroke: var(--paper); stroke-width: 9; }
  .node--partner { fill: var(--paper); stroke: var(--brand-blue); stroke-width: 7; }
  .node-outline { fill: none; stroke: var(--paper); stroke-width: 9; }
  .hub { fill: var(--brand-green); }
  .label { fill: var(--paper); font-weight: 700; font-size: 29px; text-anchor: middle; }
  .hub-label { fill: var(--paper); font-weight: 700; font-size: 27px; text-anchor: middle; }
  .brand-name { fill: var(--paper); font-weight: 800; font-size: 34px; text-anchor: middle; }
  .brand-name--partner { fill: var(--brand-blue); font-size: 36px; }
  .icon-line { fill: none; stroke: var(--paper); stroke-width: 4; stroke-linecap: round; stroke-linejoin: round; }
  .icon-fill { fill: var(--paper); }
  .map-box { fill: var(--paper); }
  .map-link { stroke: var(--paper); stroke-width: 4; }
</style>
</head>
<body>
<svg class="cycle-diagram" viewBox="0 0 1200 1018" xmlns="http://www.w3.org/2000/svg" role="img" aria-label="Cycle linking inventor, factory, licensing partner and iconic brand around innovation into the market">

  <!-- connecting ring -->
  <circle class="ring" cx="611" cy="520" r="330"/>

  <!-- hub -->
  <g class="hub-group">
    <circle class="hub" cx="611" cy="518" r="162"/>
    <g class="mind-map">
      <line class="map-link" x1="611" y1="472" x2="611" y2="430"/>
      <line class="map-link" x1="611" y1="472" x2="548" y2="445"/>
      <line class="map-link" x1="611" y1="472" x2="674" y2="445"/>
      <line class="map-link" x1="611" y1="472" x2="528" y2="494"/>
      <line class="map-link" x1="611" y1="472" x2="694" y2="494"/>
      <rect class="map-box" x="585" y="396" width="52" height="34" rx="4"/>
      <rect class="map-box" x="520" y="426" width="46" height="32" rx="4"/>
      <rect class="map-box" x="656" y="426" width="46" height="32" rx="4"/>
      <rect class="map-box" x="486" y="478" width="52" height="34" rx="4"/>
      <rect class="map-box" x="684" y="478" width="52" height="34" rx="4"/>
      <circle cx="611" cy="472" r="20" fill="var(--brand-green)" stroke="var(--paper)" stroke-width="4"/>
      <line class="icon-line" x1="603" y1="498" x2="619" y2="498"/>
      <line class="icon-line" x1="605" y1="505" x2="617" y2="505"/>
    </g>
    <text class="hub-label" x="611" y="568">Innovation</text>
    <text class="hub-label" x="611" y="601">into the</text>
    <text class="hub-label" x="611" y="634">Market</text>
  </g>

  <!-- inventor -->
  <g class="node-group node-group--inventor">
    <circle class="node" cx="611" cy="196" r="110"/>
    <g class="bulb-icon">
      <circle class="icon-line" cx="611" cy="150" r="24"/>
      <line class="icon-line" x1="602" y1="180" x2="620" y2="180"/>
      <line class="icon-line" x1="604" y1="187" x2="618" y2="187"/>
      <line class="icon-line" x1="611" y1="110" x2="611" y2="100"/>
      <line class="icon-line" x1="580" y1="124" x2="573" y2="117"/>
      <line class="icon-line" x1="642" y1="124" x2="649" y2="117"/>
      <line class="icon-line" x1="570" y1="150" x2="560" y2="150"/>
      <line class="icon-line" x1="652" y1="150" x2="662" y2="150"/>
    </g>
    <text class="label" x="611" y="236">Inventor</text>
  </g>

  <!-- factory -->
  <g class="node-group node-group--factory">
    <circle class="node" cx="941" cy="522" r="110"/>
    <path class="icon-fill" d="M900 512 V478 h10 V450 h10 v28 h8 v-14 l18 14 v-14 l18 14 v-14 l18 14 V512 Z"/>
    <circle class="icon-fill" cx="922" cy="438" r="6"/>
    <circle class="icon-fill" cx="934" cy="428" r="8"/>
    <text class="label" x="941" y="562">Factory</text>
  </g>

  <!-- iconic brand -->
  <g class="node-group node-group--brand">
    <circle class="node" cx="268" cy="516" r="110"/>
    <text class="brand-name" x="268" y="492">Corvane</text>
    <text class="label" x="268" y="540">Iconic</text>
    <text class="label" x="268" y="574">Brand</text>
  </g>

  <!-- licensing partner -->
  <g class="node-group node-group--partner">
    <circle class="node--partner" cx="611" cy="852" r="118"/>
    <circle class="node-outline" cx="611" cy="852" r="126" stroke="var(--paper)"/>
    <text class="brand-name brand-name--partner" x="611" y="865">CORVANE</text>
  </g>
</svg>
</body>
</html>
```